Logo and bussiness card stationary design

I want bussiness cards ann stationary that would mactch with the design of my website:

drmarcelofreitas.com.au

Logo Text

Dr Marcelo Freitas

```html
<!DOCTYPE html>
<html lang="en">
<head>
<meta charset="utf-8">
<title>Appointment Card</title>
<link rel="stylesheet" href="https://fonts.googleapis.com/css2?family=Nunito:wght@800;900&display=swap">
<style>
  :root {
    --teal: #4bb3c4;
    --teal-soft: #9bcdd9;
    --white: #ffffff;
    --orange: #f58a1f;
    --ink: #1e3a4a;
    --mint: #93d3cb;
    --ring: #d6d6d6;
  }
  html, body {
    margin: 0;
    padding: 0;
    width: 1200px;
    height: 704px;
    overflow: hidden;
    background: var(--teal);
  }
  .card {
    position: relative;
    width: 1200px;
    height: 704px;
    background: var(--teal);
    font-family: "Nunito", Arial, sans-serif;
    font-weight: 900;
    overflow: hidden;
  }
  .tooth-art {
    position: absolute;
    left: 0;
    top: 55px;
    width: 490px;
    height: 600px;
    border-radius: 40px 120px 180px 60px;
    background: linear-gradient(180deg, #a3d2dd 0%, #97cad7 100%);
  }
  .headline {
    position: absolute;
    left: 0;
    width: 1200px;
    top: 58px;
    margin: 0;
    text-align: center;
    color: var(--white);
    font-size: 42px;
    letter-spacing: 1.6px;
    font-weight: 900;
  }
  .date-disc {
    position: absolute;
    left: 338px;
    top: 121px;
    width: 524px;
    height: 524px;
    border-radius: 50%;
    background: var(--white);
  }
  .day {
    position: absolute;
    width: 80px;
    height: 80px;
    margin: -40px 0 0 -40px;
    border-radius: 50%;
    background: var(--white);
    color: var(--orange);
    font-size: 23px;
    display: flex;
    align-items: center;
    justify-content: center;
  }
  .day--mon { left: 371px; top: 170px; }
  .day--tue { left: 310px; top: 265px; }
  .day--wed { left: 287px; top: 370px; }
  .day--thu { left: 304px; top: 480px; }
  .day--fri { left: 358px; top: 582px; }
  .fill-line {
    position: absolute;
    height: 3px;
    background: var(--orange);
  }
  .fill-line--date { left: 427px; top: 288px; width: 333px; }
  .fill-line--time { left: 438px; top: 408px; width: 333px; }
  .label {
    position: absolute;
    color: var(--ink);
    font-size: 22px;
    line-height: 1;
  }
  .label--at { left: 384px; top: 391px; }
  .label--am { left: 661px; top: 374px; }
  .label--pm { left: 750px; top: 374px; }
  .badge {
    position: absolute;
    left: 823px;
    top: 234px;
    width: 244px;
    height: 244px;
    border-radius: 50%;
    background: var(--white);
  }
  .badge__ring {
    position: absolute;
    left: 4px;
    top: 4px;
    width: 228px;
    height: 228px;
    border-radius: 50%;
    border: 4px solid var(--ring);
    background: var(--mint);
  }
</style>
</head>
<body>
  <main class="card">
    <div class="tooth-art" role="img" aria-label="Large decorative tooth illustration with a sparkle in pale teal"></div>

    <h1 class="headline">YOUR NEXT APPOINTMENT IS ON:</h1>

    <div class="date-disc"></div>

    <div class="day day--mon">MON</div>
    <div class="day day--tue">TUE</div>
    <div class="day day--wed">WED</div>
    <div class="day day--thu">THU</div>
    <div class="day day--fri">FRI</div>

    <div class="fill-line fill-line--date"></div>
    <span class="label label--at">AT</span>
    <span class="label label--am">AM</span>
    <span class="label label--pm">PM</span>
    <div class="fill-line fill-line--time"></div>

    <div class="badge">
      <div class="badge__ring" role="img" aria-label="Tooth with heart icon in a mint circle"></div>
    </div>
  </main>
</body>
</html>
```